Accounting business needs business card

I have a business card but need something better. I want the colour changed and the design to be better. I have uploaded a picture of my new sign that is grey in colour, i would like to incorporate these colours.

```html
<!DOCTYPE html>
<html lang="en">
<head>
<meta charset="utf-8">
<title>Level Tax – Business Card</title>
<link rel="stylesheet" href="https://fonts.googleapis.com/css2?family=Montserrat:wght@400;500;700&display=swap">
<style>
  :root {
    --backdrop: #c9c9c9;
    --card-light: #ffffff;
    --card-dark: #292929;
    --ink: #2a2a2a;
    --ink-soft: #555555;
    --white: #ffffff;
    --badge-light: #dedede;
    --badge-mid: #a9a9a9;
    --badge-line: #7a7a7a;
  }
  * { margin: 0; padding: 0; box-sizing: border-box; }
  html, body {
    width: 1125px; height: 1200px; overflow: hidden;
    background: var(--backdrop);
    font-family: "Montserrat", sans-serif;
  }
  .card {
    position: absolute; left: 179px; width: 767px; height: 437px;
    border-radius: 22px; overflow: hidden;
  }
  .card--front { top: 140px; background: var(--card-light); color: var(--ink); }
  .card--back { top: 626px; background: var(--card-dark); color: var(--white); }

  .brand-mark { position: absolute; border-radius: 50%; }
  .card--front .brand-mark {
    left: 112px; top: 52px; width: 86px; height: 86px;
    border: 2.5px solid var(--ink);
  }
  .card--back .brand-mark {
    left: 324px; top: 131px; width: 120px; height: 120px;
    border: 3px solid var(--white);
  }
  .brand-name { position: absolute; font-weight: 500; white-space: nowrap; line-height: 1; }
  .card--front .brand-name {
    left: 41px; top: 155px; font-size: 29px; letter-spacing: 8px;
  }
  .card--back .brand-name {
    left: 0; width: 100%; top: 272px; text-align: center;
    font-size: 39px; letter-spacing: 13px; padding-left: 13px;
  }

  .person { position: absolute; left: 41px; top: 232px; }
  .person__name { font-size: 29px; font-weight: 700; line-height: 1; letter-spacing: 0.3px; }
  .person__role { margin-top: 10px; font-size: 17px; color: var(--ink-soft); line-height: 21px; }

  .contact { position: absolute; left: 41px; top: 328px; list-style: none; }
  .contact__item {
    display: flex; align-items: center; gap: 6px;
    font-size: 18px; color: var(--ink-soft); height: 26px;
  }
  .contact__icon { width: 14px; height: 14px; fill: var(--ink); flex: none; }

  .badges { position: absolute; left: 504px; top: 344px; width: 240px; height: 72px; }
  .badge { position: absolute; }
  .badge--rect { left: 0; top: 10px; width: 104px; height: 46px; background: var(--badge-light); }
  .badge--square { left: 124px; top: 9px; width: 48px; height: 48px; background: var(--badge-mid); }
  .badge--ring { left: 186px; top: 0; width: 48px; height: 48px; border-radius: 50%; border: 1.5px solid var(--badge-line); }
  .badge__caption {
    position: absolute; left: 175px; top: 51px; width: 70px;
    font-size: 7px; line-height: 8px; text-align: center; color: var(--ink);
  }

  .social {
    position: absolute; left: 0; width: 100%; top: 372px;
    display: flex; justify-content: center; gap: 18px; list-style: none;
  }
  .social__item {
    display: flex; align-items: center; gap: 6px;
    font-size: 13px; font-weight: 500; color: var(--white);
  }
  .social__dot { width: 10px; height: 10px; border-radius: 50%; background: var(--white); }
</style>
</head>
<body>

<section class="card card--front" aria-label="Business card front">
  <div class="brand-mark" aria-hidden="true"></div>
  <div class="brand-name">LEVEL TAX</div>

  <div class="person">
    <h1 class="person__name">LIAM HARCOURT</h1>
    <p class="person__role">CPA, MTAX, BCOM (Acc &amp; Fin)<br>Taxation and business Accountant</p>
  </div>

  <ul class="contact">
    <li class="contact__item">
      <svg class="contact__icon" viewBox="0 0 24 24" aria-hidden="true"><path d="M6.6 10.8a15.1 15.1 0 0 0 6.6 6.6l2.2-2.2c.3-.3.7-.4 1-.2 1.1.4 2.3.6 3.6.6.6 0 1 .4 1 1V20c0 .6-.4 1-1 1A17 17 0 0 1 3 4c0-.6.4-1 1-1h3.5c.6 0 1 .4 1 1 0 1.3.2 2.5.6 3.6.1.3 0 .7-.2 1z"/></svg>
      <span>0412 555 083</span>
    </li>
    <li class="contact__item">
      <svg class="contact__icon" viewBox="0 0 24 24" aria-hidden="true"><path d="M2 5h20v14H2V5zm2 2v.4l8 5.6 8-5.6V7H4zm16 2.8-8 5.6-8-5.6V17h16V9.8z"/></svg>
      <span>liam@leveltax.com.au</span>
    </li>
    <li class="contact__item">
      <svg class="contact__icon" viewBox="0 0 24 24" aria-hidden="true"><circle cx="12" cy="12" r="10"/><path d="M7 6c2 1 3 3 2 5s-3 2-3 4l2 3M15 4c-1 2 0 3 2 4s3 3 2 5-3 2-3 5" stroke="#fff" stroke-width="1.6" fill="none"/></svg>
      <span>www.leveltax.com.au</span>
    </li>
  </ul>

  <div class="badges">
    <div class="badge badge--rect" role="img" aria-label="Professional membership badge"></div>
    <div class="badge badge--square" role="img" aria-label="Software partner badge"></div>
    <div class="badge badge--ring" role="img" aria-label="Registered tax agent badge"></div>
    <p class="badge__caption">Tax agent<br>31087215</p>
  </div>
</section>

<section class="card card--back" aria-label="Business card back">
  <div class="brand-mark" aria-hidden="true"></div>
  <div class="brand-name">LEVEL TAX</div>
  <ul class="social">
    <li class="social__item"><span class="social__dot"></span>Chirp</li>
    <li class="social__item"><span class="social__dot"></span>Loopin</li>
    <li class="social__item"><span class="social__dot"></span>Proline</li>
  </ul>
</section>

</body>
</html>
```